Business card for Full Stable Works Vanhoorne

I would like to have me designed an professional business card with my existing logo for my company called : full stable works vanhoorne gcv.
I prefer a two sided business card with on the back side only the horses head and the website : fswvanhoorne-example.eu
Only one colour shouldbe all right.
The logo must appear in a nic professional way on the business card.

Other suggestion are welcome.

All copy wrights must be released by the designer after we have selected a final design.

Target Market(s)

Equestrian businesses

Industry/Entity Type

Business

Contact Information for Business Card

Gerard Vanhoorne
Title: zaakvoerder
Full Stable Works Vanhoorne GCV
Lindekouter 47
B - 9999 Voorbeeldegem
België
Phone: + 32 400 98 76 10
Mail: gerard@fswvanhoorne-example.eu

Font styles to use
Serif

Requirements
Must have
• My own logo
• See attached files
• Website: fswvanhoorne-example.eu

```html
<!DOCTYPE html>
<html lang="nl">
<head>
<meta charset="utf-8">
<title>Full Stable Works Vanhoorne – Business Card</title>
<link rel="stylesheet" href="https://fonts.googleapis.com/css2?family=Source+Sans+3:wght@400;700&display=swap">
<style>
  :root {
    --backdrop: #333333;
    --card: #ffffff;
    --ink: #111111;
  }
  * { box-sizing: border-box; margin: 0; padding: 0; }
  html, body {
    width: 1200px;
    height: 675px;
    overflow: hidden;
    background: var(--backdrop);
    font-family: "Source Sans 3", "Myriad Pro", sans-serif;
    color: var(--ink);
  }
  .sheet {
    position: relative;
    width: 1200px;
    height: 675px;
  }
  .card {
    position: absolute;
    top: 192px;
    width: 500px;
    height: 290px;
    background: var(--card);
  }
  .card--front { left: 70px; }
  .card--back  { left: 630px; }

  .brand {
    position: absolute;
    display: flex;
    align-items: center;
    gap: 12px;
  }
  .brand__mark {
    width: 30px;
    height: 30px;
    background: var(--ink);
    flex: none;
  }
  .brand__name {
    font-weight: 700;
    line-height: 1.02;
    text-transform: uppercase;
    letter-spacing: 0.02em;
  }
  .card--front .brand {
    left: 90px;
    top: 108px;
  }
  .card--front .brand__name { font-size: 26px; }
  .card--front .brand__mark { width: 46px; height: 46px; }

  .card--back .brand {
    left: 30px;
    top: 30px;
  }
  .card--back .brand__name { font-size: 17px; }

  .contact {
    position: absolute;
    right: 24px;
    bottom: 20px;
    text-align: right;
    font-size: 13.5px;
    line-height: 1.3;
    font-style: normal;
  }
  .contact__name {
    font-weight: 700;
    font-size: 15px;
  }
  .contact__role { margin-bottom: 6px; }
</style>
</head>
<body>
<main class="sheet">
  <section class="card card--front" aria-label="Front of business card">
    <div class="brand">
      <span class="brand__mark" aria-hidden="true"></span>
      <span class="brand__name">Full Stable Works<br>Vanhoorne</span>
    </div>
  </section>

  <section class="card card--back" aria-label="Back of business card">
    <div class="brand">
      <span class="brand__mark" aria-hidden="true"></span>
      <span class="brand__name">Full Stable Works<br>Vanhoorne</span>
    </div>
    <address class="contact">
      <div class="contact__name">Gerard Vanhoorne</div>
      <div class="contact__role">Director</div>
      <div class="contact__phone">+ 32 400 98 76 10</div>
      <div class="contact__mail">gerard@fswvanhoorne-example.eu</div>
      <div class="contact__web">www.fswvanhoorne-example.eu</div>
      <div class="contact__address">Lindekouter 47, B - 9999 Voorbeeldegem, België</div>
    </address>
  </section>
</main>
</body>
</html>
```